Need a Marketing System Program Overview Flyer

Our business, Builder Summit Network, helps General Contractors and home improvement businesses to generate high quality leads, acquire new customers, and improve their overall online presence.

The system includes a...
- High Converting Website
- SEO & Online Listings Management
- Strategic PPC Advertising
- Email Marketing and Automation
- Social Media Management & Retargeting Campaigns
- Reputation Management
- Tracking and Reporting

The Brochure or flyer needs to have a very professional and high class look that wows the potential customers when overviewing the program.

It needs to give a clear explanation of the program while simultaneously having the very best design concept that pulls the reader in.

I've attached our branding guide, logos and additional information...

Our site is currently being staged at www.lanternvista.com/BSN

```html
<!DOCTYPE html>
<html lang="en">
<head>
<meta charset="utf-8">
<title>Builder Summit Network – Program Overview</title>
<link rel="stylesheet" href="https://fonts.googleapis.com/css2?family=Montserrat:wght@500;600;700;800;900&family=Open+Sans:wght@400;600&display=swap">
<style>
  :root {
    --gold: #b3a46c;
    --gold-dark: #968752;
    --ink: #1d1d1d;
    --grey: #5a5a5a;
    --paper: #ffffff;
    --backdrop: #e8e8e6;
  }
  * { box-sizing: border-box; margin: 0; padding: 0; }
  html, body { width: 800px; height: 1200px; overflow: hidden; background: var(--backdrop); }
  body { font-family: "Open Sans", sans-serif; color: var(--ink); }
  .sheet-stack { width: 800px; height: 1200px; display: flex; flex-direction: column; align-items: center; justify-content: center; gap: 10px; }

  .page { position: relative; width: 430px; height: 588px; background: var(--paper); overflow: hidden; box-shadow: 0 2px 8px rgba(0,0,0,.18); }

  /* shared pieces */
  .corner-band { position: absolute; right: 0; top: 0; width: 150px; height: 14px; background: var(--ink); clip-path: polygon(14% 0, 100% 0, 100% 100%, 0 100%); }
  .section-title { font-family: "Montserrat", sans-serif; font-weight: 800; font-size: 7.5px; color: var(--gold-dark); text-transform: uppercase; letter-spacing: .3px; border-bottom: 1px solid var(--gold); padding-bottom: 3px; margin: 6px 0 7px; }
  .feature { display: flex; gap: 7px; margin-bottom: 7px; }
  .feature-icon { flex: 0 0 16px; height: 16px; border-radius: 50%; background: var(--gold); display: flex; align-items: center; justify-content: center; }
  .feature-name { font-family: "Montserrat", sans-serif; font-weight: 700; font-size: 6.5px; text-transform: uppercase; margin-bottom: 1px; }
  .feature-text { font-size: 6.3px; line-height: 1.45; color: var(--grey); }
  .lead { font-family: "Montserrat", sans-serif; font-weight: 700; font-size: 8.5px; line-height: 1.3; margin-bottom: 5px; }
  .intro { font-size: 6.5px; line-height: 1.5; color: var(--grey); margin-bottom: 4px; }

  .footer { position: absolute; left: 0; bottom: 0; width: 430px; height: 58px; display: flex; }
  .call { width: 175px; background: var(--gold); color: var(--paper); padding: 12px 0 0 22px; clip-path: polygon(0 0, 100% 0, 88% 100%, 0 100%); }
  .call-label { font-family: "Montserrat", sans-serif; font-weight: 800; font-size: 11px; letter-spacing: .5px; }
  .call-number { font-family: "Montserrat", sans-serif; font-weight: 700; font-size: 14px; color: var(--ink); }
  .contacts { flex: 1; display: flex; align-items: flex-end; }
  .contact-bar { width: 100%; height: 24px; background: var(--ink); color: var(--paper); display: flex; align-items: center; gap: 14px; padding-left: 10px; font-size: 7px; }
  .contact-item { display: flex; align-items: center; gap: 4px; white-space: nowrap; }

  /* front page */
  .masthead { height: 66px; display: flex; align-items: center; padding-left: 22px; }
  .brand { display: flex; align-items: center; gap: 6px; }
  .brand-square { width: 11px; height: 11px; background: var(--ink); }
  .brand-name { font-family: "Montserrat", sans-serif; font-weight: 800; font-size: 13px; letter-spacing: .5px; text-transform: uppercase; color: var(--ink); }
  .hero { position: relative; height: 186px; background: var(--gold); }
  .hero-image { position: absolute; right: 0; top: 0; width: 185px; height: 186px; background: linear-gradient(160deg, #ece6d2 0%, #cdb97c 45%, #8a7641 100%); clip-path: polygon(16% 0, 100% 0, 100% 100%, 0 100%); }
  .hero-copy { position: relative; z-index: 1; padding: 16px 0 0 22px; color: var(--paper); }
  .hero-title { font-family: "Montserrat", sans-serif; font-weight: 900; font-size: 19px; line-height: 1.06; text-transform: uppercase; width: 330px; }
  .hero-title .dark { color: var(--ink); }
  .hero-sub { margin-top: 10px; font-size: 7px; line-height: 1.5; font-weight: 600; width: 205px; }
  .front-content { display: flex; gap: 20px; padding: 14px 22px 0; }
  .front-content .column { flex: 1; }

  /* back page */
  .back-image { position: absolute; right: 0; top: 14px; width: 190px; height: 200px; background: linear-gradient(200deg, #d9d4c4 0%, #b9a670 50%, #6f6240 100%); clip-path: polygon(18% 0, 100% 0, 100% 100%, 0 100%); }
  .back-left { position: absolute; left: 22px; top: 22px; width: 200px; }
  .back-right { position: absolute; left: 240px; top: 222px; width: 168px; }
</style>
</head>
<body>
<div class="sheet-stack">

  <article class="page front">
    <span class="corner-band"></span>
    <header class="masthead">
      <div class="brand">
        <span class="brand-square"></span>
        <span class="brand-name">Builder Summit Network</span>
      </div>
    </header>
    <section class="hero">
      <div class="hero-image" role="img" aria-label="Stacks of gold coins rising with small builder figures on top"></div>
      <div class="hero-copy">
        <h1 class="hero-title">Accelerate your lead <span class="dark">generation while</span> increasing <span class="dark">sales and</span> reducing costs</h1>
        <p class="hero-sub">Our 7 Point Builder Summit Network System helps contractors win better leads, more customers and a stronger online presence.</p>
      </div>
    </section>
    <section class="front-content">
      <div class="column">
        <p class="lead">Take Your Business To The Next Level With High Quality Lead Generation That Works!</p>
        <p class="intro">We help general contractors and home improvement firms reach ready buyers, turn visits into calls and grow steady revenue every month.</p>
        <h2 class="section-title">High Converting Website</h2>
        <div class="feature">
          <span class="feature-icon"><svg width="9" height="9" viewBox="0 0 16 16"><path d="M3 8l3 3 7-7" fill="none" stroke="#fff" stroke-width="2.4"/></svg></span>
          <div><p class="feature-name">Fast Mobile Pages</p><p class="feature-text">Clean pages built to load fast and guide visitors to call you.</p></div>
        </div>
        <div class="feature">
          <span class="feature-icon"><svg width="9" height="9" viewBox="0 0 16 16"><path d="M3 8l3 3 7-7" fill="none" stroke="#fff" stroke-width="2.4"/></svg></span>
          <div><p class="feature-name">Clear Call To Action</p><p class="feature-text">Forms and buttons placed where buyers decide to act.</p></div>
        </div>
      </div>
      <div class="column">
        <p class="lead">Get Your Access To Next Level Marketing Via The Builder Summit Network System!</p>
        <h2 class="section-title">SEO &amp; Online Listings Management</h2>
        <div class="feature">
          <span class="feature-icon"><svg width="9" height="9" viewBox="0 0 16 16"><path d="M3 8l3 3 7-7" fill="none" stroke="#fff" stroke-width="2.4"/></svg></span>
          <div><p class="feature-name">Local Search Ranking</p><p class="feature-text">Be found first when nearby homeowners search for your trade.</p></div>
        </div>
        <div class="feature">
          <span class="feature-icon"><svg width="9" height="9" viewBox="0 0 16 16"><path d="M3 8l3 3 7-7" fill="none" stroke="#fff" stroke-width="2.4"/></svg></span>
          <div><p class="feature-name">Listings Management</p><p class="feature-text">Your details kept correct on every map and directory.</p></div>
        </div>
        <div class="feature">
          <span class="feature-icon"><svg width="9" height="9" viewBox="0 0 16 16"><path d="M3 8l3 3 7-7" fill="none" stroke="#fff" stroke-width="2.4"/></svg></span>
          <div><p class="feature-name">Content That Ranks</p><p class="feature-text">Service pages written to match what buyers type.</p></div>
        </div>
      </div>
    </section>
    <footer class="footer">
      <div class="call"><p class="call-label">CALL US</p><p class="call-number">(515) 555-0148</p></div>
      <div class="contacts"><div class="contact-bar">
        <span class="contact-item"><svg width="9" height="7" viewBox="0 0 16 12"><rect x="1" y="1" width="14" height="10" fill="none" stroke="#b3a46c" stroke-width="1.6"/><path d="M1 1l7 6 7-6" fill="none" stroke="#b3a46c" stroke-width="1.6"/></svg>info@lanternvista.com</span>
        <span class="contact-item"><svg width="8" height="8" viewBox="0 0 14 14"><circle cx="7" cy="7" r="6" fill="none" stroke="#b3a46c" stroke-width="1.5"/><path d="M1 7h12M7 1c3 3 3 9 0 12M7 1c-3 3-3 9 0 12" fill="none" stroke="#b3a46c" stroke-width="1"/></svg>www.lanternvista.com/BSN</span>
      </div></div>
    </footer>
  </article>

  <article class="page back">
    <span class="corner-band"></span>
    <div class="back-image" role="img" aria-label="Building under construction with timber frame against the sky"></div>
    <section class="back-left">
      <h2 class="section-title">Strategic PPC Advertising</h2>
      <div class="feature">
        <span class="feature-icon"><svg width="9" height="9" viewBox="0 0 16 16"><path d="M3 8l3 3 7-7" fill="none" stroke="#fff" stroke-width="2.4"/></svg></span>
        <div><p class="feature-name">Targeted Campaigns</p><p class="feature-text">Ads shown to the right people, in the right area, at the right time.</p></div>
      </div>
      <div class="feature">
        <span class="feature-icon"><svg width="9" height="9" viewBox="0 0 16 16"><path d="M3 8l3 3 7-7" fill="none" stroke="#fff" stroke-width="2.4"/></svg></span>
        <div><p class="feature-name">Budget Control</p><p class="feature-text">Spend is watched daily so every dollar works harder.</p></div>
      </div>
      <h2 class="section-title">Email Marketing &amp; Automation</h2>
      <div class="feature">
        <span class="feature-icon"><svg width="9" height="9" viewBox="0 0 16 16"><path d="M3 8l3 3 7-7" fill="none" stroke="#fff" stroke-width="2.4"/></svg></span>
        <div><p class="feature-name">Automated Follow Up</p><p class="feature-text">Stay in touch with every lead until they are ready to hire.</p></div>
      </div>
      <div class="feature">
        <span class="feature-icon"><svg width="9" height="9" viewBox="0 0 16 16"><path d="M3 8l3 3 7-7" fill="none" stroke="#fff" stroke-width="2.4"/></svg></span>
        <div><p class="feature-name">Newsletters</p><p class="feature-text">Seasonal offers and project news sent to past clients.</p></div>
      </div>
      <h2 class="section-title">Social Media Management &amp; Retargeting</h2>
      <div class="feature">
        <span class="feature-icon"><svg width="9" height="9" viewBox="0 0 16 16"><path d="M3 8l3 3 7-7" fill="none" stroke="#fff" stroke-width="2.4"/></svg></span>
        <div><p class="feature-name">Steady Posting</p><p class="feature-text">Finished jobs and tips shared on a regular weekly plan.</p></div>
      </div>
      <div class="feature">
        <span class="feature-icon"><svg width="9" height="9" viewBox="0 0 16 16"><path d="M3 8l3 3 7-7" fill="none" stroke="#fff" stroke-width="2.4"/></svg></span>
        <div><p class="feature-name">Retargeting Campaigns</p><p class="feature-text">Bring back visitors who left your site without calling.</p></div>
      </div>
    </section>
    <section class="back-right">
      <h2 class="section-title">Reputation Management</h2>
      <div class="feature">
        <span class="feature-icon"><svg width="9" height="9" viewBox="0 0 16 16"><path d="M3 8l3 3 7-7" fill="none" stroke="#fff" stroke-width="2.4"/></svg></span>
        <div><p class="feature-name">Review Requests</p><p class="feature-text">Happy clients are asked for reviews after each job.</p></div>
      </div>
      <div class="feature">
        <span class="feature-icon"><svg width="9" height="9" viewBox="0 0 16 16"><path d="M3 8l3 3 7-7" fill="none" stroke="#fff" stroke-width="2.4"/></svg></span>
        <div><p class="feature-name">Review Replies</p><p class="feature-text">Every comment gets a prompt and polite answer.</p></div>
      </div>
      <h2 class="section-title">Tracking &amp; Reporting</h2>
      <div class="feature">
        <span class="feature-icon"><svg width="9" height="9" viewBox="0 0 16 16"><path d="M3 8l3 3 7-7" fill="none" stroke="#fff" stroke-width="2.4"/></svg></span>
        <div><p class="feature-name">Call Tracking</p><p class="feature-text">See where each call and each sale comes from.</p></div>
      </div>
      <div class="feature">
        <span class="feature-icon"><svg width="9" height="9" viewBox="0 0 16 16"><path d="M3 8l3 3 7-7" fill="none" stroke="#fff" stroke-width="2.4"/></svg></span>
        <div><p class="feature-name">Monthly Reports</p><p class="feature-text">Clear numbers on leads, cost and growth each month.</p></div>
      </div>
    </section>
    <footer class="footer">
      <div class="call"><p class="call-label">CALL US</p><p class="call-number">(515) 555-0148</p></div>
      <div class="contacts"><div class="contact-bar">
        <span class="contact-item"><svg width="9" height="7" viewBox="0 0 16 12"><rect x="1" y="1" width="14" height="10" fill="none" stroke="#b3a46c" stroke-width="1.6"/><path d="M1 1l7 6 7-6" fill="none" stroke="#b3a46c" stroke-width="1.6"/></svg>info@lanternvista.com</span>
        <span class="contact-item"><svg width="8" height="8" viewBox="0 0 14 14"><circle cx="7" cy="7" r="6" fill="none" stroke="#b3a46c" stroke-width="1.5"/><path d="M1 7h12M7 1c3 3 3 9 0 12M7 1c-3 3-3 9 0 12" fill="none" stroke="#b3a46c" stroke-width="1"/></svg>www.lanternvista.com/BSN</span>
      </div></div>
    </footer>
  </article>

</div>
</body>
</html>
```